Prosthetic Brochure

Looking for a trifold brochure that highlights our Prosthetic department. Has to have good stock pictures of prosthetic care. Should have Prosthetic Services from our website www.brindlemoorclinic.com I would like it in the same colors of our website.

Target Market(s)

Patients and physicians

Industry/Entity Type

Medical

Requirements
Must have
• Pictures of people helping prosthetic patients and information from the flyer I uploaded and our website under Prosthetic services.
Nice to have
• Same color scheme as our website. Blue with orange highlights
Should not have
• Just prosthetics no pictures of braces ( orthotics)

```html
<!DOCTYPE html>
<html lang="en">
<head>
<meta charset="utf-8">
<title>Brindlemoor Prosthetic Lab – Trifold Brochure</title>
<link href="https://fonts.googleapis.com/css2?family=Oswald:wght@500&family=Roboto+Condensed:wght@400;700&family=Open+Sans:wght@400;600&family=Montserrat:ital,wght@0,700;1,700&display=swap" rel="stylesheet">
<style>
  :root{
    --stage:#5fc4a7;
    --navy:#2c4470;
    --navy-deep:#233a63;
    --sky:#a9d3ee;
    --pale:#e6f0f9;
    --purple:#6b5a9e;
    --purple-soft:#8d7fc0;
    --ink:#1e2a3a;
    --white:#ffffff;
  }
  *{box-sizing:border-box;margin:0;padding:0}
  html,body{width:1200px;height:3195px;overflow:hidden;background:var(--stage)}
  .canvas{position:relative;width:1200px;height:3195px}
  .spread{position:absolute;left:0;width:1200px;height:795px;overflow:hidden;box-shadow:0 6px 24px rgba(0,0,0,.18)}
  .spread--outside{top:520px}
  .spread--inside{top:1880px}
  .panel{position:absolute;top:0;width:400px;height:795px;overflow:hidden}
  .panel--1{left:0}.panel--2{left:400px}.panel--3{left:800px}
  .photo{position:absolute;background:linear-gradient(135deg,#dfe8ef,#8fa8c2);}
  .photo--round{border-radius:50%;border:9px solid var(--sky)}
  .wave{position:absolute;left:0;top:0;width:400px;height:795px}

  /* outside: about */
  .about{background:linear-gradient(180deg,var(--pale),#f6f9fc)}
  .badge{position:absolute;left:137px;top:32px;width:126px;height:126px;border-radius:50%;background:var(--navy);border:6px solid var(--white);box-shadow:0 0 0 3px var(--navy)}
  .about__text{position:absolute;left:55px;top:172px;width:300px;font:400 16.5px/1.25 "Open Sans",sans-serif;color:var(--ink)}

  /* outside: locations */
  .locations{background:linear-gradient(180deg,var(--navy) 0%,var(--navy) 40%,#5d76ad 75%,var(--purple-soft) 100%);color:var(--white);text-align:center}
  .locations__title{margin-top:30px;font:500 27px/1 "Oswald",sans-serif;letter-spacing:1px}
  .location{margin-top:22px;font:400 15px/1.27 "Roboto Condensed",sans-serif}
  .locations__brand{position:absolute;left:0;right:0;top:742px;font:italic 700 17px/1 "Montserrat",sans-serif;letter-spacing:.5px}

  /* outside: cover */
  .cover{background:linear-gradient(180deg,#fff 0%,#f3f6fb 40%,#7c6fae 70%,var(--purple) 100%)}
  .cover__team{position:absolute;left:0;top:0;width:400px;height:160px;background:linear-gradient(180deg,#c9d6e4,#eef2f7 80%,rgba(255,255,255,0))}
  .cover__brand{position:absolute;left:0;right:0;top:170px;text-align:center;font:700 26px/1.15 "Montserrat",sans-serif;color:var(--navy-deep)}
  .cover__brand small{display:block;margin-top:8px;font:700 13px/1 "Roboto Condensed",sans-serif;color:#3a67a8}
  .cover__call{position:absolute;left:0;right:0;top:730px;text-align:center;font:700 24px/1 "Open Sans",sans-serif;letter-spacing:1.5px;color:var(--white)}
  .cover__url{position:absolute;left:100px;top:763px;width:200px;height:32px;background:var(--white);border-radius:8px 8px 0 0;text-align:center;font:600 14px/32px "Open Sans",sans-serif;color:var(--navy)}

  /* inside: staff */
  .staff{background:linear-gradient(180deg,#f2f6fb,var(--pale) 70%,#fff)}
  .member{position:absolute;left:30px;width:340px;height:160px}
  .member .photo{left:0;top:0;width:115px;height:115px;border:3px solid #7fa2c9}
  .member__info{position:absolute;left:135px;top:0;width:210px;text-align:center;font-family:"Roboto Condensed",sans-serif;color:var(--ink)}
  .member__name{font:700 11px/1.15 "Roboto Condensed",sans-serif;letter-spacing:.3px}
  .member__cred{font:400 10.5px/1.15 "Roboto Condensed",sans-serif;letter-spacing:.4px}
  .member__bio{margin-top:12px;font:400 10px/1.2 "Roboto Condensed",sans-serif}
  .staff__url{position:absolute;left:0;right:0;top:755px;text-align:center;font:600 15px/1 "Open Sans",sans-serif;color:var(--white)}

  /* inside: why */
  .why{background:linear-gradient(180deg,#d3deea,#b5c5d8 55%,#cbd6e3)}
  .why__title{position:absolute;left:0;right:0;top:48px;text-align:center;font:700 16px/1 "Montserrat",sans-serif;color:var(--navy-deep)}
  .why__list{position:absolute;left:55px;top:82px;width:300px;list-style:none;font:400 14px/1.27 "Montserrat",sans-serif;color:var(--ink)}
  .why__list li{position:relative;padding-left:22px;margin-bottom:4px}
  .why__list li::before{content:"";position:absolute;left:2px;top:6px;width:8px;height:8px;border-radius:50%;background:var(--purple)}
  .why__outro{position:absolute;left:60px;width:280px;top:478px;text-align:center;font:400 14px/1.27 "Montserrat",sans-serif;color:var(--ink)}
  .why__cta{position:absolute;left:0;right:0;top:541px;text-align:center;font:700 17px/1.3 "Montserrat",sans-serif;color:#6f64b0;letter-spacing:.5px}
  .why__cta span{display:block;color:var(--navy-deep)}
  .why .photo{left:82px;top:615px;width:236px;height:160px;background:linear-gradient(135deg,#e3ebf2,#7a8fa8)}
</style>
</head>
<body>
<div class="canvas">

  <section class="spread spread--outside">
    <div class="panel panel--1 about">
      <div class="badge" role="img" aria-label="Certification badge"></div>
      <p class="about__text">Brindlemoor Prosthetic Lab has been providing quality, compassionate care to residents of Fenwick and Southern Illinois since 1983. A recognized leader in the field, our experts work as a team to create the most functional solution to your prosthetic needs using the latest technology available. Our patient-centered, team approach means we work closely with your doctor, nurse, therapist and family to deliver a great fitting prosthetic device that work for you.</p>
      <svg class="wave" viewBox="0 0 400 795" aria-hidden="true">
        <path d="M0,512 C90,540 200,585 400,568 L400,795 L0,795 Z" fill="#2c4470"/>
        <path d="M0,500 C90,528 200,573 400,556" fill="none" stroke="#a9d3ee" stroke-width="10"/>
      </svg>
      <div class="photo photo--round" style="left:65px;top:505px;width:270px;height:270px" role="img" aria-label="Photo of a clinician fitting a prosthetic leg for a seated patient"></div>
    </div>

    <div class="panel panel--2 locations">
      <h2 class="locations__title">LOCATIONS</h2>
      <p class="location">310 Alder Lane Fenwick. MO 63190<br>PH: (555) 014-2200</p>
      <p class="location">Harbor Advanced Care Center<br>82 Quarry Place. # 4B Fenwick MO 63192<br>Ph: (555) 014-2210</p>
      <p class="location">19 Juniper Road. Suite 210 Fenwick. MO 63195<br>PH: (555) 014-2220</p>
      <p class="location">4401 Orchard Drive. Ste. 8 Millbrook. MO 63048<br>PH: (555) 014-2230</p>
      <p class="location">7 Copper Terrace. Ste. 2<br>Ridgeway. IL 62230<br>PH: (555) 014-2240</p>
      <div class="photo photo--round" style="left:60px;top:420px;width:280px;height:280px" role="img" aria-label="Photo of a technician assembling a prosthetic leg in the lab"></div>
      <p class="locations__brand">Brindlemoor Prosthetic Lab, Inc.</p>
    </div>

    <div class="panel panel--3 cover">
      <div class="cover__team" role="img" aria-label="Photo of the clinical team standing in a row"></div>
      <p class="cover__brand">Brindlemoor<small>Brindlemoor Prosthetic Lab, Inc.</small></p>
      <svg class="wave" viewBox="0 0 400 795" aria-hidden="true">
        <path d="M0,360 C120,330 250,260 400,300 L400,795 L0,795 Z" fill="#6b5a9e" opacity=".35"/>
      </svg>
      <div class="photo photo--round" style="left:35px;top:300px;width:310px;height:310px" role="img" aria-label="Photo of a therapist walking beside a patient using a prosthetic leg"></div>
      <p class="cover__call">Call Us: 555-014-2200</p>
      <div class="cover__url">www.brindlemoorclinic.com</div>
    </div>
  </section>

  <section class="spread spread--inside">
    <div class="panel panel--1 staff">
      <div class="member" style="top:35px">
        <div class="photo" role="img" aria-label="Portrait photo of Owen Hartley"></div>
        <div class="member__info">
          <p class="member__name">OWEN HARTLEY, CPO</p>
          <p class="member__cred">National Board Certified<br>Prosthetist &amp; Orthotist</p>
          <p class="member__bio">Owen has dual Master's Degrees in Prosthetics and Orthotic and in Business Administration. His undergrad was in Athletic training. Owen is up to date on the latest cutting edge prosthetic technology and loves the advancements being made in prosthetics</p>
        </div>
      </div>
      <div class="member" style="top:233px">
        <div class="photo" role="img" aria-label="Portrait photo of Clara Benning"></div>
        <div class="member__info">
          <p class="member__name">CLARA BENNING, CPO</p>
          <p class="member__cred">National Board Certified<br>Prosthetist &amp; Orthotist</p>
          <p class="member__bio">Clara graduated from Eastvale State University with her Master of Science in Prosthetics and Orthotics. She has been practicing Prosthetics and Orthotics since 2018. Clara is a people person and loves working with patients.</p>
        </div>
      </div>
      <div class="member" style="top:435px">
        <div class="photo" role="img" aria-label="Portrait photo of Felix Marlow"></div>
        <div class="member__info">
          <p class="member__name">FELIX MARLOW, CPO</p>
          <p class="member__cred">Prosthetist &amp; Orthotist</p>
          <p class="member__bio">Felix grew up in Fenwick and went to Fenwick University where he graduated in biomedical engineering. He graduated from Westbrook Medical College with a Masters Degree in Prosthetics and Orthotics. His hobbies include playing soccer and he is passionate about helping others.</p>
        </div>
      </div>
      <svg class="wave" viewBox="0 0 400 795" aria-hidden="true">
        <path d="M0,700 C130,690 260,690 400,655 L400,795 L0,795 Z" fill="#233a63"/>
        <path d="M0,690 C130,680 260,680 400,645" fill="none" stroke="#a9d3ee" stroke-width="6"/>
      </svg>
      <p class="staff__url">www.brindlemoorclinic.com</p>
    </div>

    <div class="panel panel--2 why">
      <h2 class="why__title">Why use Brindlemoor Prosthetic Lab?</h2>
      <ul class="why__list">
        <li>First-class patient care - Our Facility is accredited by the National Limb Care Board. We have met rigid standards that put patient needs and safety first</li>
        <li>High-end technology - We are always current on the latest socket and component technology</li>
        <li>Local Fabrication Facility - Our fabrication and assembly happens right here in Fenwick.</li>
        <li>Experience - 78 years of combined technical &amp; practitioner experience</li>
        <li>Fast turnaround - Same week check sockets, complete definitive prosthesis in 30 days ( pending insurance authorizations)</li>
        <li>A firm belief in teamwork- We love to work with the patient, rehabilitative staff and physicians to achieve the patient's goals.</li>
      </ul>
      <p class="why__outro">All of these combined allow us to provide the best possible patient outcome</p>
      <p class="why__cta">Call us today for a Free<br>consult and prosthetic check-up<span>Call (555) 014 -2200</span></p>
      <div class="photo" role="img" aria-label="Photo of a clinician adjusting a prosthetic arm for a patient"></div>
    </div>

    <div class="panel panel--3 staff">
      <div class="member" style="top:35px">
        <div class="photo" role="img" aria-label="Portrait photo of Walter Pryce"></div>
        <div class="member__info">
          <p class="member__name">WALTER PRYCE, CPO</p>
          <p class="member__cred">National Board Certified<br>Prosthetist &amp; Orthotist</p>
          <p class="member__bio">With Over 46 Years of Prosthetics experience. Walter has been a leader and past president of our National organization and is highly respected for his experience and knowledge.</p>
        </div>
      </div>
      <div class="member" style="top:233px">
        <div class="photo" role="img" aria-label="Portrait photo of Nora Ellison"></div>
        <div class="member__info">
          <p class="member__name">NORA ELLISON, CPO</p>
          <p class="member__cred">National Board Certified<br>Prosthetist &amp; Orthotist</p>
          <p class="member__bio">Nora graduated from Lakeshore University with her Masters Degree in Prosthetics &amp; Orthotics. Nora did her undergrad at Fenwick University in biomedical Engineering. Nora is a Fenwick native and loves this city</p>
        </div>
      </div>
      <div class="member" style="top:435px">
        <div class="photo" role="img" aria-label="Portrait photo of Miles Carver"></div>
        <div class="member__info">
          <p class="member__name">MILES CARVER, CPO</p>
          <p class="member__cred">National Board Certified<br>Prosthetist &amp; Orthotist</p>
          <p class="member__bio">Miles graduated from the Riverton University with a Master Degree in Prosthetics and Orthotics. His undergrad is in exercise physiology from Central Plains State. Miles is a huge outdoor enthusiast and loves helping people regain their independence</p>
        </div>
      </div>
      <svg class="wave" viewBox="0 0 400 795" aria-hidden="true">
        <path d="M0,655 C140,690 270,690 400,700 L400,795 L0,795 Z" fill="#233a63"/>
        <path d="M0,645 C140,680 270,680 400,690" fill="none" stroke="#a9d3ee" stroke-width="6"/>
      </svg>
      <p class="staff__url">www.brindlemoorclinic.com</p>
    </div>
  </section>

</div>
</body>
</html>
```